Project Quarter 2

A business card with the following details

Rob Kettering
Consultant/Speaker/Trainer

The Brand Quarter Hub (Insert Logo)
News and Ideas for Brand Marketers
www.brandquarterhub.com

Rob.Kettering@brandquarterhub.com
+61 452 918 604
Facebook icon
Twitter icon
Linkedin icon
Google+ icon
Pinterist icon

Target Market(s)

Small and Medium sized business owners
Brand marketers

Industry/Entity Type

Business

Requirements
Must have
• Utilise The Brand Quarter Hub Logo and colour scheme
Nice to have
• More male than female in outlook.
Have a connnected feel to it and a link to a precinct good too.
Bold and simple design the ideal

```html
<!DOCTYPE html>
<html lang="en">
<head>
<meta charset="utf-8">
<title>The Brand Quarter Hub – Business Card</title>
<link rel="stylesheet" href="https://fonts.googleapis.com/css2?family=Lato:wght@400;700&display=swap">
<style>
  :root {
    --sky: #4db2cf;
    --navy: #1d4f7e;
    --ink: #2b2b2b;
    --paper: #ffffff;
    --backdrop: #dcdfe2;
  }
  * { margin: 0; padding: 0; box-sizing: border-box; }
  html, body {
    width: 1200px;
    height: 900px;
    overflow: hidden;
    background: var(--backdrop);
    font-family: "Lato", Arial, sans-serif;
  }
  .canvas { position: relative; width: 1200px; height: 900px; }

  .card {
    position: absolute;
    width: 640px;
    height: 366px;
    overflow: hidden;
    box-shadow: 0 10px 28px rgba(0,0,0,0.18);
  }

  /* Back side */
  .card-back {
    left: 480px;
    top: 50px;
    background: var(--sky);
  }
  .card-back .brand-disc {
    position: absolute;
    right: -40px;
    top: -70px;
    width: 300px;
    height: 300px;
    border-radius: 50%;
    background: var(--navy);
  }
  .card-back .wordmark {
    position: absolute;
    left: 40px;
    bottom: 70px;
    font-size: 40px;
    color: var(--navy);
  }
  .card-back .tagline {
    position: absolute;
    left: 42px;
    bottom: 40px;
    font-size: 20px;
    color: var(--navy);
  }

  /* Front side */
  .card-front {
    left: 80px;
    top: 470px;
    background: var(--paper);
  }
  .brand-lockup {
    position: absolute;
    left: 40px;
    top: 40px;
    display: flex;
    align-items: center;
    gap: 14px;
  }
  .brand-lockup .dot {
    width: 40px;
    height: 40px;
    border-radius: 50%;
    background: var(--navy);
  }
  .wordmark {
    font-weight: 700;
    letter-spacing: -0.5px;
  }
  .brand-lockup .wordmark {
    font-size: 38px;
    color: var(--navy);
  }
  .contact {
    position: absolute;
    left: 64px;
    top: 126px;
    color: var(--ink);
  }
  .contact .person {
    font-size: 26px;
    font-weight: 400;
    color: var(--navy);
    letter-spacing: 0.5px;
  }
  .contact .role { font-size: 16px; margin-top: 2px; }
  .contact .lines { margin-top: 16px; font-size: 17px; line-height: 1.3; }
  .website {
    position: absolute;
    left: 40px;
    bottom: 36px;
    font-size: 17px;
    font-weight: 700;
    color: var(--ink);
  }
  .social {
    position: absolute;
    right: 36px;
    bottom: 32px;
    display: flex;
    gap: 12px;
    list-style: none;
  }
  .social li {
    width: 34px;
    height: 34px;
    border-radius: 4px;
    background: var(--sky);
  }
  .social li:nth-child(odd) { background: var(--navy); }
</style>
</head>
<body>
<main class="canvas">
  <section class="card card-back" aria-label="Card back">
    <div class="brand-disc"></div>
    <p class="wordmark">thebrandquarterhub</p>
    <p class="tagline">News and Ideas for Brand Marketers</p>
  </section>

  <section class="card card-front" aria-label="Card front">
    <div class="brand-lockup">
      <span class="dot"></span>
      <span class="wordmark">thebrandquarterhub</span>
    </div>
    <div class="contact">
      <h1 class="person">ROB KETTERING</h1>
      <p class="role">Consultant/Speaker/Trainer</p>
      <p class="lines">+61 452 918 604<br>Rob.Kettering@brandquarterhub.com</p>
    </div>
    <p class="website">www.brandquarterhub.com</p>
    <ul class="social" aria-label="Social channels">
      <li></li><li></li><li></li><li></li><li></li>
    </ul>
  </section>
</main>
</body>
</html>
```